Re-design a training handout - Leadership Blueprint

We need a graphic design for a training workbook for leaders to use in a workshop and as a journal.
It is two A3 double sided with fold lines and content already laid out. It is dull & does not capture imagination.

We want it to be something a leader gets as part of a program and cannot not wait to begin filing out the blank sections.
We are calling it a leader "blue print".
It needs to be in Adobe Indesign5 (so we can improve it ourselves over the coming months.
We will send the Indesign file with everything already done EXCEPT the magic of a great layout.
A sample of ONE page (of Four) has been attached. It is page with the most writing.
Updates

Project Deadline Extended
Reason: I have provided a guarantee to pay and answered some questions which will help. A couple of designers requested extra information and guidance. Thanks again - there will be no further extension. Kind regards. Tod

Target Market(s)

Leaders and executives of team from 10 to 500

Industry/Entity Type

Graphic Design

Requirements
Must have
• Indesign5
work within the A3 with the fold lines already indicated
Be able to written on in the blank or line sections.
Keep the same text.

```html
<!DOCTYPE html>
<html lang="en">
<head>
<meta charset="utf-8">
<title>Leadership Blueprint</title>
<link href="https://fonts.googleapis.com/css2?family=Fira+Sans+Condensed:wght@500;700&display=swap" rel="stylesheet">
<style>
  :root {
    --navy: #0d1f45;
    --gold: #d4910f;
    --gold-bright: #e8a317;
    --paper: #ffffff;
    --fold: #b8b8b8;
  }
  * { box-sizing: border-box; margin: 0; padding: 0; }
  html, body { width: 1200px; height: 861px; overflow: hidden; background: var(--paper); }
  body { font-family: "Fira Sans Condensed", "Arial Narrow", sans-serif; color: var(--navy); }
  .sheet { position: relative; width: 1200px; height: 861px; }
  .sheet > * { position: absolute; }
  .trim { left: 0; top: 0; width: 1200px; height: 848px; border: 1px solid #9a9a9a; }
  .fold-line { left: 595px; top: 0; height: 848px; border-left: 1.5px dashed var(--fold); }
  .fold-tick { top: 851px; width: 3px; height: 10px; background: var(--gold); }

  .section-title { font-weight: 700; font-size: 35px; line-height: 1; letter-spacing: -0.3px; color: var(--navy); }
  .gold-tag { background: var(--gold); }

  .col-head { top: 38px; width: 60px; text-align: center; font-weight: 500; line-height: 1; }
  .col-head b { display: block; font-size: 15px; font-weight: 700; }
  .col-head span { display: block; font-size: 9px; }

  .metric-line { left: 37px; width: 245px; height: 4px; background: var(--navy); }
  .check-box { width: 29px; height: 29px; border: 2.5px solid var(--gold); }
  .metric-divider { left: 447px; top: 77px; width: 2px; height: 190px; background: var(--navy); }

  .plan-head { top: 337px; height: 23px; background: var(--navy); color: var(--paper);
    font-size: 11px; font-weight: 700; padding: 5px 0 0 7px; }
  .plan-table { left: 56px; top: 371px; width: 532px; height: 452px; border: 4px solid var(--gold);
    display: grid; grid-template-columns: 104px 1fr; grid-template-rows: 66px 78px 76px 77px 77px 1fr; }
  .plan-table div { border-bottom: 3px solid var(--gold); }
  .plan-table div:nth-child(odd) { border-right: 3px solid var(--gold); }
  .plan-table div:nth-last-child(-n+2) { border-bottom: none; }

  .panel-head { height: 35px; background: var(--navy); color: var(--paper);
    font-size: 30px; font-weight: 500; line-height: 1; padding: 5px 0 0 16px; }
  .panel-box { width: 241px; height: 223px; border: 4px solid var(--navy); }
  .ruled { position: absolute; left: 6px; right: 6px; top: 1px; height: 200px;
    background: repeating-linear-gradient(to bottom, transparent 0 22px, var(--navy) 22px 25px); }

  .dev-box { left: 624px; top: 685px; width: 500px; height: 131px; border: 3px solid var(--gold); }
  .dev-head { position: absolute; left: 3px; top: 3px; width: 488px; height: 32px; background: var(--gold-bright);
    color: var(--paper); font-size: 27px; font-weight: 500; line-height: 1; padding: 3px 0 0 7px; }
  .dev-ruled { position: absolute; left: 13px; width: 464px; top: 44px; height: 75px;
    background: repeating-linear-gradient(to bottom, transparent 0 13px, var(--gold) 13px 14.5px, transparent 14.5px 24.5px); }
</style>
</head>
<body>
<main class="sheet">
  <div class="trim"></div>
  <div class="fold-line"></div>
  <div class="fold-tick" style="left:288px"></div>
  <div class="fold-tick" style="left:592px"></div>

  <!-- People metric -->
  <div class="gold-tag" style="left:0;top:40px;width:29px;height:27px"></div>
  <h2 class="section-title" style="left:37px;top:36px">PEOPLE METRIC</h2>
  <div class="col-head" style="left:327px"><b>MY</b><span>BASELINE</span></div>
  <div class="col-head" style="left:382px"><b>MY</b><span>TARGET</span></div>
  <div class="col-head" style="left:467px"><b>MY</b><span>BASELINE</span></div>
  <div class="col-head" style="left:521px"><b>MY</b><span>TARGET</span></div>

  <div class="metric-line" style="top:118px"></div>
  <div class="metric-line" style="top:179px"></div>
  <div class="metric-line" style="top:246px"></div>
  <div class="metric-divider"></div>

  <div class="check-box" style="left:331px;top:101px"></div>
  <div class="check-box" style="left:395px;top:101px"></div>
  <div class="check-box" style="left:471px;top:101px"></div>
  <div class="check-box" style="left:536px;top:101px"></div>
  <div class="check-box" style="left:331px;top:163px"></div>
  <div class="check-box" style="left:395px;top:163px"></div>
  <div class="check-box" style="left:471px;top:163px"></div>
  <div class="check-box" style="left:536px;top:163px"></div>
  <div class="check-box" style="left:331px;top:224px"></div>
  <div class="check-box" style="left:395px;top:224px"></div>
  <div class="check-box" style="left:471px;top:224px"></div>
  <div class="check-box" style="left:536px;top:224px"></div>

  <!-- Action plan -->
  <div class="gold-tag" style="left:0;top:280px;width:29px;height:29px"></div>
  <h2 class="section-title" style="left:44px;top:276px">MY ACTION PLAN</h2>
  <div class="gold-tag" style="left:340px;top:281px;width:247px;height:28px"></div>
  <div class="plan-head" style="left:59px;width:95px">WHEN</div>
  <div class="plan-head" style="left:177px;width:410px">WHAT</div>
  <div class="plan-table">
    <div></div><div></div><div></div><div></div><div></div><div></div>
    <div></div><div></div><div></div><div></div><div></div><div></div>
  </div>

  <!-- Leadership blueprint -->
  <h1 class="section-title" style="left:617px;top:37px;line-height:40px">LEADERSHIP<br>BLUEPRINT</h1>
  <div style="left:883px;top:36px;width:243px;height:32px;border:3px solid var(--gold)"></div>
  <div class="gold-tag" style="left:1136px;top:36px;width:64px;height:33px"></div>

  <div class="panel-head" style="left:620px;top:139px;width:245px">WHY</div>
  <div class="panel-box" style="left:623px;top:176px"><div class="ruled"></div></div>

  <div class="panel-head" style="left:883px;top:139px;width:243px;padding-left:10px">WHO I WORK</div>
  <div class="panel-box" style="left:883px;top:176px"><div class="ruled"></div></div>

  <div class="panel-head" style="left:620px;top:411px;width:245px;height:33px"></div>
  <div class="panel-box" style="left:623px;top:448px"><div class="ruled"></div></div>

  <div class="panel-box" style="left:883px;top:411px;height:260px"></div>

  <section class="dev-box">
    <h3 class="dev-head">DEVELOPMENT PRIORITIES</h3>
    <div class="dev-ruled"></div>
  </section>
</main>
</body>
</html>
```